International Automotive Parts Marketing business needs professional, sleek Android app design.

We have developed an Android app for our sales team and are now looking for an overall design our developers can apply. The design should mirror our corporate website kvrelo.com. There is a LOT of data the reps need to work through so not really any images other that login screen - of course icons are great. Lots of lists and searches etc. - it needs to look professional, feel amazing and easy to use. Our motto - Simple is always better. We included our logo and a few screenshots of the app page 1 and 2.

Target Market(s)

Professional Sales and Marketing - our own sales team (100 reps) will use this app

Font styles to use
Sans Serif

Colors

Designer to choose colors to be used in the design.

Requirements
Must have
• App design must be professional and easy to use in the field all day. Similar look and feel of corporate website kvrelo.com. Same colors and images. Icons to manage navigation
Should not have
• Non-professional look and feel. No vector cartoon type images. No specific parts related images

```html
<!DOCTYPE html>
<html lang="en">
<head>
<meta charset="utf-8">
<title>Company List</title>
<link href="https://fonts.googleapis.com/css2?family=Nunito:wght@400;600;700&display=swap" rel="stylesheet">
<style>
  :root {
    --ink: #1f1f1f;
    --ink-soft: #2b2b2b;
    --muted: #b9b9b9;
    --accent: #a8172f;
    --header-bg: #000000;
    --page-bg: #ffffff;
    --rule: #cfcfcf;
    --card-shadow: rgba(0, 0, 0, 0.16);
  }
  * { margin: 0; padding: 0; box-sizing: border-box; }
  html, body {
    width: 675px; height: 1200px; overflow: hidden;
    background: var(--page-bg);
    font-family: "Nunito", sans-serif;
    color: var(--ink);
  }
  .screen { position: relative; width: 675px; height: 1200px; overflow: hidden; }

  .app-header {
    position: absolute; left: 0; top: 0; width: 675px; height: 268px;
    background: var(--header-bg); color: #fff;
  }
  .status-time {
    position: absolute; left: 22px; top: 8px;
    font-size: 19px; font-weight: 600; line-height: 24px;
  }
  .status-icons { position: absolute; right: 20px; top: 11px; }
  .back-button { position: absolute; left: 26px; top: 74px; }
  .screen-title {
    position: absolute; left: 0; right: 0; top: 64px;
    text-align: center; font-size: 31px; font-weight: 400; line-height: 42px;
  }
  .search-field {
    position: absolute; left: 24px; top: 149px; width: 624px; height: 74px;
    background: #fff; border-radius: 37px;
  }
  .search-text {
    position: absolute; left: 33px; top: 22px;
    font-size: 21px; line-height: 30px; color: var(--ink-soft);
  }
  .search-text .caret {
    display: inline-block; width: 1.5px; height: 27px; background: var(--ink);
    vertical-align: -7px; margin: 0 0.5px;
  }
  .search-text .placeholder { color: var(--muted); }
  .search-icon { position: absolute; right: 28px; top: 19px; }

  .group-bar {
    position: absolute; left: 37px; top: 300px; width: 597px; height: 57px;
    border-bottom: 1px solid var(--rule);
  }
  .group-label { position: absolute; left: 0; top: 10px; font-size: 20px; line-height: 26px; }
  .refresh-icon { position: absolute; right: 0; top: 11px; }

  .company-card {
    position: absolute; left: 30px; width: 612px; height: 151px;
    background: #fff; border-radius: 8px;
    box-shadow: 0 1px 7px var(--card-shadow);
  }
  .company-name {
    position: absolute; left: 35px; top: 25px;
    font-size: 29px; font-weight: 400; line-height: 40px; color: var(--ink);
  }
  .company-meta, .company-touch {
    position: absolute; left: 37px; font-size: 17px; line-height: 22px; color: var(--ink);
  }
  .company-meta { top: 71px; }
  .company-touch { top: 103px; }
  .company-meta .value { color: var(--accent); font-weight: 700; }
  .gap { display: inline-block; width: 9px; }
  .company-card.is-fading { opacity: 0.35; box-shadow: 0 1px 7px rgba(0,0,0,0.05); }
  .company-card.is-fading .company-name { color: var(--accent); opacity: 0.6; }
</style>
</head>
<body>
<div class="screen">
  <header class="app-header">
    <div class="status-time">9:41</div>
    <svg class="status-icons" width="94" height="18" viewBox="0 0 94 18" aria-hidden="true">
      <rect x="0" y="11" width="3.5" height="5" rx="1" fill="#fff"/>
      <rect x="5.5" y="8" width="3.5" height="8" rx="1" fill="#fff"/>
      <rect x="11" y="5" width="3.5" height="11" rx="1" fill="#fff"/>
      <rect x="16.5" y="2" width="3.5" height="14" rx="1" fill="#fff"/>
      <path d="M27 6.5a13 13 0 0 1 18 0l-1.8 1.9a10.4 10.4 0 0 0-14.4 0z" fill="#fff"/>
      <path d="M30.4 10a8 8 0 0 1 11.2 0l-1.8 1.9a5.4 5.4 0 0 0-7.6 0z" fill="#fff"/>
      <path d="M33.8 13.5a3 3 0 0 1 4.4 0L36 16z" fill="#fff"/>
      <rect x="55.5" y="1.5" width="33" height="14" rx="4" fill="none" stroke="#fff" stroke-width="1.4"/>
      <rect x="58" y="4" width="28" height="9" rx="2" fill="#fff"/>
      <rect x="90" y="6" width="2.5" height="5" rx="1" fill="#fff"/>
    </svg>
    <svg class="back-button" width="24" height="22" viewBox="0 0 24 22" aria-label="Back" role="img">
      <path d="M22 11H4M11.5 3 3.5 11l8 8" fill="none" stroke="#fff" stroke-width="3" stroke-linecap="round" stroke-linejoin="round"/>
    </svg>
    <h1 class="screen-title">Company List</h1>
    <div class="search-field">
      <div class="search-text">Fil<span class="caret"></span><span class="placeholder">ter</span></div>
      <svg class="search-icon" width="36" height="36" viewBox="0 0 36 36" aria-label="Search" role="img">
        <circle cx="14.5" cy="14.5" r="10.5" fill="none" stroke="var(--accent)" stroke-width="4.5"/>
        <path d="M22.5 22.5 32 32" stroke="var(--accent)" stroke-width="6" stroke-linecap="round"/>
      </svg>
    </div>
  </header>

  <div class="group-bar">
    <span class="group-label">Gruop By</span>
    <svg class="refresh-icon" width="28" height="28" viewBox="0 0 28 28" aria-label="Refresh" role="img">
      <path d="M22 9.5A10 10 0 1 0 23.5 18" fill="none" stroke="var(--accent)" stroke-width="4.2" stroke-linecap="round"/>
      <path d="M26 2v11H15z" fill="var(--accent)"/>
    </svg>
  </div>

  <article class="company-card" style="top:405px">
    <h2 class="company-name">418 Auto Service Centre</h2>
    <p class="company-meta">Coquitlam<span class="gap"></span>: Bc&nbsp; type<span class="gap"></span><span class="value">M</span><span class="gap"></span>Rating <span class="value">B</span></p>
    <p class="company-touch">Last Touch<span class="gap"></span>19 Oct 2019</p>
  </article>
  <article class="company-card" style="top:584px">
    <h2 class="company-name">418 Auto Service Centre</h2>
    <p class="company-meta">Coquitlam<span class="gap"></span>: Bc&nbsp; type<span class="gap"></span><span class="value">M</span><span class="gap"></span>Rating <span class="value">B</span></p>
    <p class="company-touch">Last Touch<span class="gap"></span>19 Oct 2019</p>
  </article>
  <article class="company-card" style="top:764px">
    <h2 class="company-name">418 Auto Service Centre</h2>
    <p class="company-meta">Coquitlam<span class="gap"></span>: Bc&nbsp; type<span class="gap"></span><span class="value">M</span><span class="gap"></span>Rating <span class="value">B</span></p>
    <p class="company-touch">Last Touch<span class="gap"></span>19 Oct 2019</p>
  </article>
  <article class="company-card" style="top:943px">
    <h2 class="company-name">418 Auto Service Centre</h2>
    <p class="company-meta">Coquitlam<span class="gap"></span>: Bc&nbsp; type<span class="gap"></span><span class="value">M</span><span class="gap"></span>Rating <span class="value">B</span></p>
    <p class="company-touch">Last Touch<span class="gap"></span>19 Oct 2019</p>
  </article>
  <article class="company-card is-fading" style="top:1125px">
    <h2 class="company-name">418 Auto Service Centre</h2>
  </article>
</div>
</body>
</html>
```